Business Card Design

Professional solutions in (servers, security, networks, programming)

Industry/Entity Type

Business

Contact Information for Business Card

Tarek Hounayni
Internet services and network solutions
DPV - RTLK - RTLB
netcare@qo-lam.com / 05917406238
www.qo-lam.com

```html
<!DOCTYPE html>
<html lang="en">
<head>
<meta charset="UTF-8">
<title>Tarek Hounayni — Business Card</title>
<link rel="stylesheet" href="https://fonts.googleapis.com/css2?family=Arimo:wght@400;700&display=swap">
<style>
  :root {
    --backdrop: #d9d6d2;
    --card: #ececec;
    --ink: #2b2b2b;
    --band: #2d2d2d;
    --gold: #d4a24c;
    --light: #ffffff;
  }
  * { margin: 0; padding: 0; box-sizing: border-box; }
  html, body {
    width: 1200px;
    height: 900px;
    overflow: hidden;
    background: var(--backdrop);
    font-family: "Arimo", Arial, sans-serif;
  }
  .canvas {
    position: relative;
    width: 1200px;
    height: 900px;
  }
  .card {
    position: absolute;
    left: 100px;
    top: 164px;
    width: 1000px;
    height: 572px;
    background: var(--card);
    box-shadow: 0 12px 30px rgba(0,0,0,0.18);
  }
  .rule {
    position: absolute;
    left: 110px;
    width: 830px;
    height: 6px;
    background: var(--band);
  }
  .rule--top { top: 158px; }
  .rule--bottom { top: 304px; }
  .name-band {
    position: absolute;
    left: 110px;
    top: 172px;
    width: 830px;
    height: 124px;
    background: var(--band);
    text-align: center;
    padding-top: 22px;
  }
  .name {
    color: var(--light);
    font-size: 50px;
    font-weight: 400;
    letter-spacing: 2px;
    line-height: 1;
  }
  .tagline {
    margin-top: 12px;
    color: var(--gold);
    font-size: 26px;
    letter-spacing: 0.5px;
    line-height: 1;
  }
  .contact-row {
    position: absolute;
    left: 120px;
    top: 336px;
    width: 820px;
    display: flex;
    justify-content: space-between;
    color: var(--ink);
    font-size: 21px;
    white-space: nowrap;
  }
  .contact-row .label { font-weight: 700; }
  .contact-row .divider { color: #777; }
  .credentials {
    position: absolute;
    left: 0;
    width: 1000px;
    top: 420px;
    text-align: center;
    color: var(--ink);
    font-size: 38px;
    font-weight: 700;
    letter-spacing: 1px;
  }
</style>
</head>
<body>
  <main class="canvas">
    <section class="card" aria-label="Business card">
      <div class="rule rule--top"></div>
      <header class="name-band">
        <h1 class="name">TAREK HOUNAYNI</h1>
        <p class="tagline">Internet Services And Network Solutions</p>
      </header>
      <div class="rule rule--bottom"></div>
      <p class="contact-row">
        <span><span class="label">p :</span> 05917406238</span>
        <span class="divider">|</span>
        <span><span class="label">m :</span> netcare@qo-lam.com</span>
        <span class="divider">|</span>
        <span><span class="label">w :</span> www.qo-lam.com</span>
      </p>
      <p class="credentials">DPV - RTLK - RTLB</p>
    </section>
  </main>
</body>
</html>
```